Quelvar Website

We need a web design for our company based in Sydney. Our company does many and varied acitivities. From private investments, licencing, business consultacy, payment solutions.

Our services focus on our client’s critical opportunities. We provide a range of services including strategy, marketing, compliance, organization and technology.

We can unlock your growth and potential and deliver on core strategy. We add value and bring extensive expertise in optimizing your results.

We provide also provide the following services:

 private investments,
 licensing,
 business consultancy,
 payment solutions.

Target Market(s)

Businesses

Coding

Coded - Design and coding required

Number of Pages Required

3 page

Colors

Designer to choose colors to be used in the design.

Requirements
Must have
• Corporate look and feel. two touch points, email info@quelvar.com.au and a phone number TBA
• MUST include logos and branding from attached
Nice to have
• photos

```html
<!DOCTYPE html>
<html lang="en">
<head>
<meta charset="utf-8">
<title>Quelvar Website</title>
<link href="https://fonts.googleapis.com/css2?family=Nunito:wght@700;800&family=Open+Sans:ital,wght@0,400;0,600;0,700;1,400&family=Roboto:wght@400;500;700&display=swap" rel="stylesheet">
<style>
:root{
  --blue:#0aa6e6;
  --blue-dark:#0b6fb8;
  --ink:#2a2a2a;
  --text:#444;
  --grey-bg:#e9e9e9;
  --nav:#2b2b2b;
  --footer:#343434;
  --footer-dark:#222;
  --white:#fff;
  --muted:#777;
}
*{margin:0;padding:0;box-sizing:border-box}
html,body{width:1200px;height:3564px;overflow:hidden}
body{font-family:"Open Sans",sans-serif;color:var(--text);background:var(--white);position:relative}
.abs{position:absolute}
a{color:inherit;text-decoration:none}

/* header */
.site-header{position:absolute;top:0;left:0;width:1200px;height:116px;background:var(--white)}
.brand{position:absolute;left:68px;top:28px;display:flex;align-items:center;gap:14px}
.brand-dot{width:22px;height:22px;border-radius:50%;background:var(--blue)}
.brand-name{font-family:"Roboto",sans-serif;font-weight:700;font-size:46px;color:#6d7a86;letter-spacing:1px}
.contact-mini{position:absolute;top:44px;display:flex;gap:12px;align-items:center;font-size:14px;color:var(--ink)}
.contact-mini strong{display:block;font-weight:700;font-size:15px}
.contact-mini span{font-size:13px}

/* nav */
.main-nav{position:absolute;top:116px;left:0;width:1200px;height:43px;background:var(--nav)}
.main-nav a{position:absolute;top:12px;color:var(--white);font-family:"Roboto",sans-serif;font-size:15px}
.main-nav a.active::after{content:"";position:absolute;left:-6px;right:-6px;bottom:-13px;height:3px;background:var(--blue)}
.quote-btn{position:absolute;left:945px;top:0;width:130px;height:43px;background:var(--blue-dark);clip-path:polygon(14px 0,100% 0,100% 100%,0 100%);color:var(--white);font-family:"Roboto",sans-serif;font-size:15px;display:flex;align-items:center;justify-content:center;padding-left:10px}
.search-btn{position:absolute;left:1081px;top:4px;width:47px;height:35px;background:#d9d9d9;display:flex;align-items:center;justify-content:center}

/* hero */
.hero{position:absolute;top:159px;left:0;width:1200px;height:570px;background:radial-gradient(circle at 78% 30%,#3d8ec4 0%,#1c4f7a 30%,#0d2238 65%,#07121f 100%)}
.hero-visual{position:absolute;left:760px;top:0;width:440px;height:570px;background:radial-gradient(ellipse at 50% 35%,rgba(120,210,255,.45),rgba(20,50,80,.0) 60%)}
.hero-copy{position:absolute;left:71px;top:175px;color:var(--white)}
.hero-copy h1{font-family:"Nunito",sans-serif;font-weight:800;font-size:33px;line-height:40px;width:680px}
.hero-copy p{font-family:"Nunito",sans-serif;font-weight:700;font-size:15px;line-height:23px;margin-top:4px}
.btn-primary{position:absolute;left:64px;top:366px;width:162px;height:52px;background:var(--blue);color:var(--white);font-family:"Roboto",sans-serif;font-weight:500;font-size:15px;display:flex;align-items:center;justify-content:center;border-radius:2px}

/* section heads */
.eyebrow{position:absolute;left:0;width:1200px;text-align:center;font-size:13px;color:#555}
.section-title{position:absolute;left:0;width:1200px;text-align:center;font-family:"Roboto",sans-serif;font-weight:500;font-size:37px;color:var(--ink);letter-spacing:.5px}
.title-rule{position:absolute;left:540px;width:120px;height:2px;background:var(--blue-dark)}

.intro-text{position:absolute;left:68px;width:1064px;text-align:center;font-size:13px;line-height:18px;color:#444}
.photo{position:absolute}

/* services */
.services{position:absolute;top:1285px;left:0;width:1200px;height:362px;display:flex}
.service{width:400px;height:362px;position:relative;text-align:center;color:var(--white);background:var(--blue)}
.service.alt{background:var(--grey-bg);color:var(--ink)}
.service svg{position:absolute;left:160px;top:28px}
.service h3{position:absolute;top:133px;left:0;width:100%;font-family:"Roboto",sans-serif;font-weight:500;font-size:22px;letter-spacing:.5px}
.service p{position:absolute;top:174px;left:55px;width:290px;font-size:13px;line-height:19px}
.service .view{position:absolute;top:290px;left:152px;width:96px;height:34px;border:2px solid var(--white);font-family:"Roboto",sans-serif;font-weight:500;font-size:13px;display:flex;align-items:center;justify-content:center}
.service.alt .view{border-color:#555}

/* approach */
.approach-frame{position:absolute;left:109px;top:1849px;width:347px;height:289px;border:2px solid var(--blue)}
.approach-text{position:absolute;left:520px;top:1808px;width:622px;font-size:14.5px;line-height:22px;color:#333}
.approach-text p+p{margin-top:22px}
.btn-outline{position:absolute;left:520px;top:2096px;width:136px;height:45px;border:2px solid #555;border-radius:4px;font-family:"Roboto",sans-serif;font-weight:500;font-size:15px;color:var(--ink);display:flex;align-items:center;justify-content:center}

/* news */
.news{position:absolute;top:2198px;left:0;width:1200px;height:475px;background:linear-gradient(180deg,#1d8fd8 0%,#0aa6e6 55%,#09a9ea 100%)}
.news .eyebrow{color:#dff3ff}
.news .section-title{color:var(--white)}
.news-card{position:absolute;top:147px;height:240px;display:flex}
.news-card .thumb{height:240px}
.news-card .body{background:var(--white);width:233px;height:216px;margin-top:12px;padding:12px 14px}
.news-card h4{font-family:"Roboto",sans-serif;font-weight:700;font-size:13.5px;color:var(--blue);text-transform:uppercase}
.news-card p{font-size:13.5px;line-height:18px;color:#333;margin-top:8px}
.news-card .more{display:block;margin-top:6px;font-weight:700;font-size:13.5px;color:var(--blue)}
.dots{position:absolute;top:431px;left:563px;display:flex;gap:7px}
.dots span{width:13px;height:13px;border-radius:50%;background:#1a1a1a}
.dots span.on{background:var(--white)}

/* reviews */
.quote-text{position:absolute;left:200px;top:2932px;width:800px;text-align:center;font-style:italic;font-size:16px;line-height:30px;color:#444}
.cite{position:absolute;left:0;top:3032px;width:1200px;text-align:center;font-size:10.5px;color:#444}

/* contact band */
.cta-band{position:absolute;top:3113px;left:0;width:1200px;height:118px;background:#2f2f2f}
.cta-call{position:absolute;left:0;top:0;width:550px;height:118px;background:var(--blue-dark);clip-path:polygon(0 0,100% 0,94% 100%,0 100%);color:var(--white)}
.cta-call small{position:absolute;left:265px;top:24px;font-size:19px;color:#0b0b0b}
.cta-call strong{position:absolute;left:212px;top:50px;font-family:"Roboto",sans-serif;font-weight:700;font-size:37px;letter-spacing:.5px}
.quote-form h3{position:absolute;left:575px;top:32px;font-family:"Roboto",sans-serif;font-weight:700;font-size:20px;color:var(--white)}
.field{position:absolute;top:78px;width:200px;height:34px;background:#ececec;font-size:12px;color:#888;padding:9px 10px}
.subscribe{position:absolute;left:1012px;top:78px;width:105px;height:34px;background:var(--blue-dark);color:var(--white);font-family:"Roboto",sans-serif;font-weight:700;font-size:15px;display:flex;align-items:center;justify-content:center}

/* footer */
.site-footer{position:absolute;top:3231px;left:0;width:1200px;height:271px;background:var(--footer);color:var(--white)}
.site-footer h5{position:absolute;top:62px;font-family:"Roboto",sans-serif;font-weight:700;font-size:23px}
.link-list{position:absolute;top:116px;list-style:none;font-size:13.5px;line-height:24px}
.contact-row{position:absolute;left:399px;display:flex;gap:14px;align-items:flex-start;font-size:12px;line-height:16px}
.icon-circle{width:27px;height:27px;border-radius:50%;background:#8d8d8d;flex-shrink:0;display:flex;align-items:center;justify-content:center}
.social-row{position:absolute;left:684px;display:flex;gap:14px;align-items:center;font-size:12.5px;letter-spacing:.5px}
.social-row .dot{width:28px;height:28px;border-radius:50%}
.footer-brand{position:absolute;left:892px;top:105px;font-family:"Roboto",sans-serif;font-weight:700;font-size:46px;color:#b7b7b7;letter-spacing:1px}
.copyright{position:absolute;top:3502px;left:0;width:1200px;height:62px;background:var(--footer-dark);color:var(--white);font-size:14px;display:flex;align-items:center;justify-content:center}
</style>
</head>
<body>

<header class="site-header">
  <div class="brand"><span class="brand-dot"></span><span class="brand-name">Quelvar</span></div>
  <div class="contact-mini" style="left:790px">
    <svg width="26" height="26" viewBox="0 0 24 24" fill="none" stroke="#555" stroke-width="1.6"><path d="M5 3h4l2 5-2.5 1.5a11 11 0 0 0 6 6L16 13l5 2v4a2 2 0 0 1-2 2A17 17 0 0 1 3 5a2 2 0 0 1 2-2z"/></svg>
    <div><strong>1-800.555.0142</strong><span>info@quelvar.com.au</span></div>
  </div>
  <div class="contact-mini" style="left:978px">
    <svg width="28" height="28" viewBox="0 0 24 24" fill="none" stroke="#555" stroke-width="1.6"><circle cx="12" cy="12" r="9"/><path d="M12 7v5l3 2"/></svg>
    <div><strong>7:30 AM - 7:30 PM</strong><span>Monday to Saturday</span></div>
  </div>
</header>

<nav class="main-nav">
  <a class="active" href="#" style="left:80px">Home</a>
  <a href="#" style="left:173px">Features</a>
  <a href="#" style="left:287px">Support</a>
  <a href="#" style="left:392px">Pricing</a>
  <a href="#" style="left:497px">Contact Us</a>
  <a href="#" style="left:625px">Resources</a>
  <a class="quote-btn" href="#" style="top:0">GET A QUOTE</a>
  <div class="search-btn"><svg width="22" height="22" viewBox="0 0 24 24" fill="none" stroke="#333" stroke-width="2"><circle cx="10" cy="10" r="6"/><path d="M15 15l6 6"/></svg></div>
</nav>

<section class="hero">
  <div class="hero-visual" role="img" aria-label="Photo of a businessman in a suit with a glowing circuit-style brain in place of his head"></div>
  <div class="hero-copy">
    <h1>We provide a range of services including strategy, marketing, compliance, organization and technology.</h1>
    <p>There are many variations of passages of Lorem Ipsum available,<br>but the majority have suffered alteration in some form, by injected humour.</p>
  </div>
  <a class="btn-primary" href="#">GET STARTED</a>
</section>

<section class="leaders">
  <div class="eyebrow" style="top:747px">an interdisciplinary consulting</div>
  <h2 class="section-title" style="top:768px">LEADERS IN CHANGE MANAGEMENT RECRUITMENT</h2>
  <div class="title-rule" style="top:838px"></div>
  <p class="intro-text" style="top:876px">Harbourline Consulting was founded in 2005 with a vision of being the first, and the best, Change Management recruitment and consulting business in Australia. Since then, our business has evolved and thrived in an environment where change is now considered the “norm”.</p>
  <p class="intro-text" style="top:931px">Today, Harbourline Consulting is in the business of partnering with clients to provide the frameworks, expertise and resources to deliver sustainable enterprise-wide change and transformation. Our team in Australia and New Zealand is comprised of agile, innovative thinkers who know how to listen, think, then act. We aim to leave behind a legacy of change and transformation best practice within the organisations we have the privilege of working with.</p>
  <div class="photo" role="img" aria-label="Group photo of six business people in suits standing in a row" style="left:143px;top:998px;width:891px;height:287px;background:linear-gradient(180deg,#f2f4f7 0%,#c9d3df 45%,#2d3f5c 100%)"></div>
</section>

<section class="services">
  <div class="service">
    <svg width="80" height="80" viewBox="0 0 80 80" fill="none" stroke="#fff" stroke-width="3"><circle cx="44" cy="28" r="18"/><path d="M44 18v20M49 22h-8a3 3 0 0 0 0 6h6a3 3 0 0 1 0 6h-9"/><path d="M6 62h14l14 6h22l16-10"/></svg>
    <h3>PRIVATE INVESTMENTS</h3>
    <p>All Operators have valuable seismic related data that is stored on analog or digital media in a variety of formats. They also have paper, film, sepia, and other types of records that may be stored in boxes.</p>
    <a class="view" href="#">VIEW</a>
  </div>
  <div class="service alt">
    <svg width="80" height="80" viewBox="0 0 80 80" fill="#111"><circle cx="40" cy="20" r="12"/><path d="M18 58c0-14 10-22 22-22s22 8 22 22z"/><rect x="12" y="58" width="56" height="6"/></svg>
    <h3>BUSINESS CONSULTANCY</h3>
    <p>All Operators have valuable seismic related data that is stored on analog or digital media in a variety of formats. They also have paper, film, sepia, and other types of records that may be stored in boxes.</p>
    <a class="view" href="#">VIEW</a>
  </div>
  <div class="service">
    <svg width="80" height="80" viewBox="0 0 80 80" fill="none" stroke="#fff" stroke-width="3"><circle cx="40" cy="24" r="16" fill="#fff"/><path d="M40 14v20M45 18h-7a3 3 0 0 0 0 6h4a3 3 0 0 1 0 6h-7" stroke="#0aa6e6"/><path d="M8 56l14-8h14l10 6h16l10-6M8 66h54l10-8"/></svg>
    <h3>PAYMENT SOLUTIONS</h3>
    <p>All Operators have valuable seismic related data that is stored on analog or digital media in a variety of formats. They also have paper, film, sepia, and other types of records that may be stored in boxes.</p>
    <a class="view" href="#">VIEW</a>
  </div>
</section>

<section class="approach">
  <div class="eyebrow" style="top:1691px">an interdisciplinary consulting</div>
  <h2 class="section-title" style="top:1712px">OUR UNIQUE APPROACH FOR SUCCESS</h2>
  <div class="approach-frame"></div>
  <div class="photo" role="img" aria-label="Video still of two businessmen reviewing documents" style="left:81px;top:1820px;width:349px;height:295px;background:linear-gradient(135deg,#1e3d6b 0%,#4a78a8 50%,#d7dde6 100%)"></div>
  <svg class="abs" style="left:228px;top:1940px" width="56" height="56" viewBox="0 0 56 56"><circle cx="28" cy="28" r="25" fill="none" stroke="#fff" stroke-width="3"/><path d="M22 17l17 11-17 11z" fill="#fff"/></svg>
  <div class="approach-text">
    <p><strong>Harbourline Consulting was founded in 2005 with a vision of being the first, and the best, Change Management</strong> recruitment and consulting business in Australia. Since then, our business has evolved and thrived in an environment where change is now considered the “norm”.</p>
    <p>Today, Harbourline Consulting is in the business of partnering with clients to provide the frameworks, expertise and resources to deliver sustainable enterprise-wide change and transformation. Our team in Australia and New Zealand is comprised of agile, innovative thinkers who know how to listen, think, then act. We aim to leave behind a legacy of change and transformation best practice within the organisations we have the privilege of working with.</p>
  </div>
  <a class="btn-outline" href="#">Learn More</a>
</section>

<section class="news">
  <div class="eyebrow" style="top:34px">an interdisciplinary consulting</div>
  <h2 class="section-title" style="top:56px">LATEST NEWS &amp; ARTICLES</h2>
  <article class="news-card" style="left:62px">
    <div class="thumb" role="img" aria-label="Photo of a businessman extending his hand for a handshake" style="width:290px;background:linear-gradient(135deg,#f3f3f3 0%,#b9c2cc 50%,#1d2530 100%)"></div>
    <div class="body">
      <h4>Commercial Services</h4>
      <p>Today, Harbourline Consulting is in the business of partnering with clients to provide the frameworks, expertise and resources to deliver sustainable enterprise-wide change and transformation.</p>
      <a class="more" href="#">Read More</a>
    </div>
  </article>
  <article class="news-card" style="left:615px">
    <div class="thumb" role="img" aria-label="Photo of business people silhouetted against a bright office window" style="width:288px;background:linear-gradient(180deg,#dbe9f6 0%,#7fa6cc 55%,#1b3b63 100%)"></div>
    <div class="body">
      <h4>Commercial Services</h4>
      <p>Today, Harbourline Consulting is in the business of partnering with clients to provide the frameworks, expertise and resources to deliver sustainable enterprise-wide change and transformation.</p>
      <a class="more" href="#">Read More</a>
    </div>
  </article>
  <div class="dots"><span></span><span class="on"></span><span></span></div>
</section>

<section class="reviews">
  <div class="eyebrow" style="top:2717px">an interdisciplinary consulting</div>
  <h2 class="section-title" style="top:2739px">OUR CLIENT REVIEWS</h2>
  <svg class="abs" style="left:541px;top:2816px" width="78" height="80" viewBox="0 0 78 80" role="img" aria-label="Client portrait"><polygon points="39,2 74,21 74,59 39,78 4,59 4,21" fill="#c9b8a6" stroke="#e2e2e2" stroke-width="3"/></svg>
  <p class="quote-text">“The benefits of psychological capital appear to be as central to the success of entrepreneurs as more traditional forms of capital.”</p>
  <p class="cite">(“The Role of Affect in the Entrepreneurial Process,” J.L. Marlow, The Journal of Enterprise Studies, Vol. 33 (2).</p>
</section>

<section class="cta-band">
  <div class="cta-call"><small>You can call us toll free</small><strong>+61 1300 555 018</strong></div>
  <div class="quote-form">
    <h3>Request a Free Quote</h3>
    <div class="field" style="left:575px">Name</div>
    <div class="field" style="left:794px">Email</div>
    <a class="subscribe" href="#">Subscribe</a>
  </div>
</section>

<footer class="site-footer">
  <h5 style="left:71px">Quick Links</h5>
  <ul class="link-list" style="left:73px"><li>Home</li><li>How it works</li><li>Features</li><li>Pricing</li><li>Contact us</li></ul>
  <ul class="link-list" style="left:230px"><li>Terms of use</li><li>Reseller</li><li>Sitemap</li><li>Uptime Report</li></ul>

  <h5 style="left:399px">Contact Us</h5>
  <div class="contact-row" style="top:112px">
    <span class="icon-circle"><svg width="13" height="15" viewBox="0 0 12 16"><path d="M6 0a6 6 0 0 1 6 6c0 4-6 10-6 10S0 10 0 6a6 6 0 0 1 6-6z" fill="#fff"/><circle cx="6" cy="6" r="2" fill="#8d8d8d"/></svg></span>
    <span>Level 9, Suite 14<br>220 Harbour Row<br>Docklands, Victoria 3008</span>
  </div>
  <div class="contact-row" style="top:180px;align-items:center">
    <span class="icon-circle"><svg width="13" height="13" viewBox="0 0 24 24" fill="#fff"><path d="M5 3h4l2 5-2.5 1.5a11 11 0 0 0 6 6L16 13l5 2v4a2 2 0 0 1-2 2A17 17 0 0 1 3 5a2 2 0 0 1 2-2z"/></svg></span>
    <span>+61 3 9000 2417</span>
  </div>
  <div class="contact-row" style="top:220px;align-items:center">
    <span class="icon-circle"><svg width="14" height="11" viewBox="0 0 20 14" fill="none" stroke="#fff" stroke-width="2"><rect x="1" y="1" width="18" height="12"/><path d="M1 1l9 7 9-7"/></svg></span>
    <span>info@quelvar.com.au</span>
  </div>

  <h5 style="left:684px">Follow Us</h5>
  <div class="social-row" style="top:112px"><span class="dot" style="background:#2d6fc2"></span>FRIENDLINE</div>
  <div class="social-row" style="top:155px"><span class="dot" style="background:#2aa8e6"></span>CHIRPER</div>
  <div class="social-row" style="top:198px"><span class="dot" style="background:#e86a2b"></span>CIRCLES+</div>

  <div class="footer-brand">Quelvar</div>
</footer>

<div class="copyright">Copyright © 2016, Quelvar Website. All rights reserved. Privacy Policy.</div>

</body>
</html>
```